e-commerce website for selling flooring materials and related accessories

We are developing a new e-commerce site based in the US. We plan to sell all types of flooring - such as Hardwood, Laminate, Waterproof flooring and Porcelain tile, marble, Carpet, and related accessories.

OUR BACK END IS MAGENTO 2.

Target Market(s)

consumer, builder & contractors, hospitality industry, architect, designers, private sector

Industry/Entity Type

Flooring

Coding

Coded - Design and coding required

Number of Pages Required

5+ page

Font styles to use
Sans Serif

Requirements
Must have
• Logo placement, 3 Color combination, Banner placement, promotional pricing tags, check out page, blog placement, social media icons, 1800 number, product and related accessories placement. For reference purposes, please visit our competitor websites -
1.www.plankvaultoutlet.net
2.tilehavenhome.com
3.www.grainmarketdepot.com
4.www.craftsupplyhub.com
5.www.mosskeepcorp.com
Nice to have
• Our main customers are women and families and we want to make sure the design is attractive.
we like to have 2 or 3 bands at the top.
please provide design for the bottom page.
Should not have
• As our products are more natural colors, please do not bring extreme colors into the design

```html
<!DOCTYPE html>
<html lang="en">
<head>
<meta charset="utf-8">
<title>Floorvale</title>
<link href="https://fonts.googleapis.com/css2?family=Rubik:wght@400;500&family=Montserrat:wght@500;600&display=swap" rel="stylesheet">
<style>
:root{
  --orange:#f15a22;
  --rust:#b0410f;
  --dark:#231a16;
  --footer:#1f1b19;
  --text:#2b2b2b;
  --muted:#555;
  --white:#fff;
}
*{margin:0;padding:0;box-sizing:border-box}
html,body{width:1200px;height:3951px;overflow:hidden}
body{position:relative;background:var(--white);font-family:Arial,Helvetica,sans-serif;color:var(--text)}
.abs{position:absolute}
.heading{font-family:'Rubik',sans-serif;font-weight:400;color:#222}
.heading span{color:var(--orange)}
.rule{position:absolute;height:3px;width:72px;background:var(--orange)}
.btn{position:absolute;background:var(--orange);color:#fff;font-family:'Rubik',sans-serif;font-size:17px;display:flex;align-items:center;justify-content:center;border-radius:3px;letter-spacing:.5px}

.topbar{left:0;top:0;width:1200px;height:54px;background:var(--dark);color:#fff;font-size:13px}
.topbar .call{left:110px;top:19px;font-weight:bold}
.toplinks{right:110px;top:19px;display:flex;gap:26px;font-size:12.5px}
.toplinks .sep{color:#aaa}

.header{left:0;top:54px;width:1200px;height:110px;background:#fff;box-shadow:0 2px 4px rgba(0,0,0,.08)}
.brand{left:110px;top:26px;display:flex;align-items:center;gap:10px}
.brand-mark{width:50px;height:50px;background:var(--orange)}
.brand-name{font-family:'Rubik',sans-serif;font-weight:500;font-size:29px;color:var(--orange);letter-spacing:.5px}
.nav{left:480px;top:49px;display:flex;gap:47px;font-family:'Rubik',sans-serif;font-size:15px;color:#222}
.nav .active{color:var(--orange)}

.hero{left:0;top:164px;width:1200px;height:689px;background:linear-gradient(160deg,#8a7462 0%,#5a4536 40%,#3a2a20 75%,#6b5240 100%)}
.hero-title{left:0;width:1200px;top:590px;text-align:center;font-family:'Rubik',sans-serif;font-size:58px;color:#fff}
.hero-sub{left:0;width:1200px;top:668px;text-align:center;font-family:'Rubik',sans-serif;font-size:27px;color:#fff}

.welcome-title{left:120px;top:993px;font-size:37px}
.welcome-text{left:120px;width:410px;font-size:13.5px;line-height:26px;color:var(--muted);text-align:justify}
.tile-img{left:578px;top:1099px;width:288px;height:287px;background:linear-gradient(135deg,#9a9a9a,#6f6f6f 60%,#8c8c8c)}
.room-img{left:649px;top:939px;width:439px;height:376px;background:linear-gradient(180deg,#e9e7e3 0%,#d6d1c8 50%,#a6733f 75%,#7b4f26 100%)}

.cat{top:1485px;width:298px;height:468px}
.cat .photo{height:398px}
.cat .label{height:70px;background:var(--rust);color:#fff;font-family:'Rubik',sans-serif;font-size:23px;display:flex;align-items:center;justify-content:center}

.section-title{left:0;width:1200px;text-align:center;font-size:37px}
.product{width:235px;text-align:center}
.product .pic{height:218px;position:relative;overflow:hidden}
.product .tag{position:absolute;left:-30px;top:12px;width:110px;height:26px;background:var(--orange);color:#fff;font-size:12px;font-family:'Rubik',sans-serif;transform:rotate(-45deg);display:flex;align-items:center;justify-content:center}
.product .name{margin-top:26px;font-family:'Rubik',sans-serif;font-size:19px;color:#333;letter-spacing:.5px}
.product .price{margin-top:8px;font-family:'Rubik',sans-serif;font-size:21px;color:var(--orange)}

.promo{left:110px;top:2808px;width:978px;height:189px;background:linear-gradient(90deg,#4a3424 0%,#6f5038 45%,#3b2a1f 100%)}
.promo-text{text-align:center;font-family:'Rubik',sans-serif}
.promo-text .line{font-size:29px;color:#fff}
.promo-text .off{font-size:46px;color:var(--orange);margin-top:4px}

.post{top:3141px;width:310px}
.post .pic{height:237px;position:relative}
.post .date{position:absolute;right:0;bottom:0;width:118px;height:37px;background:var(--orange);color:#fff;font-family:'Rubik',sans-serif;font-size:15px;display:flex;align-items:center;justify-content:center}
.post .title{margin-top:28px;font-family:'Rubik',sans-serif;font-size:19px;color:#222}
.post .body{margin-top:16px;font-size:13px;line-height:26px;color:var(--muted)}
.post .more{margin-top:14px;font-family:'Rubik',sans-serif;font-size:15px;color:var(--orange);text-decoration:underline}

.footer{left:0;top:3612px;width:1200px;height:339px;background:var(--footer);color:#fff}
.fcol{top:63px}
.fhead{font-family:'Montserrat',sans-serif;font-weight:600;font-size:15px;letter-spacing:.3px}
.flist{list-style:none;margin-top:20px;font-size:12.5px;line-height:26px}
.flist li::before{content:"\25B8";margin-right:18px;font-size:11px}
.cards{display:flex;gap:6px;margin-top:20px}
.card{width:40px;height:25px;background:#e6e6e6;color:#1f3c88;font-size:9px;font-weight:bold;display:flex;align-items:center;justify-content:center;border-radius:2px}
.socials{display:flex;gap:6px;position:absolute;left:0;top:150px}
.socials span{width:36px;height:36px;border:2px solid #fff;border-radius:50%}
.contact li{list-style:none;font-size:11.5px;line-height:15px;margin-bottom:13px;display:flex;gap:12px}
.contact svg{flex:none}
.copyright{left:0;width:1200px;top:302px;text-align:center;font-size:12px;color:#ddd}
</style>
</head>
<body>

<div class="abs topbar">
  <div class="abs call">&#9742; Call Us : 1800-555-0142</div>
  <div class="abs toplinks">
    <span>&#128274; LOGIN</span><span class="sep">|</span>
    <span>&#128100; REGISTER</span><span class="sep">|</span>
    <span>&#8644; COMPARE</span><span class="sep">|</span>
    <span>&#128722; CART</span><span class="sep">|</span>
    <span>&#9906; SEARCH</span>
  </div>
</div>

<header class="abs header">
  <div class="abs brand"><div class="brand-mark"></div><div class="brand-name">FLOORVALE</div></div>
  <nav class="abs nav">
    <span class="active">HOME</span><span>ABOUT US</span><span>SERVICES</span><span>PRODUCTS</span><span>BLOG</span><span>CONTACT US</span>
  </nav>
</header>

<section class="abs hero" role="img" aria-label="Living room interior with dark wood floor, sofa, dining set and fireplace"></section>
<div class="abs hero-title">Floorvale</div>
<div class="abs hero-sub">Sed ut perspiciatis unde omnis iste natus error sit</div>
<div class="btn" style="left:520px;top:721px;width:160px;height:46px">SHOP NOW</div>

<h2 class="abs heading welcome-title">Welcome <span>Floorvale</span></h2>
<div class="rule" style="left:120px;top:1057px"></div>
<p class="abs welcome-text" style="top:1089px">Sed ut perspiciatis unde omnis iste natus error sit voluptatem accus antium doloremque laudantium, totam rem aperiam, eaque ipsa quae ab illo inventore veritatis et quasi architecto'</p>
<p class="abs welcome-text" style="top:1192px">Nemo enim ipsam voluptatem quia voluptas sit aspernatur aut odit aut fugit, sed quia consequuntur magni dolores eos qui ratione voluptatem sequi nesciunt. Neque porro quisquam est, qui dolorem ipsum quia dolor sit amet, consectetur, adipisci velit,</p>
<div class="btn" style="left:120px;top:1333px;width:145px;height:44px">READ MORE</div>
<div class="abs tile-img" role="img" aria-label="Grey stone floor tiles"></div>
<div class="abs room-img" role="img" aria-label="Office interior with wood plank flooring"></div>

<div class="abs cat" style="left:0"><div class="photo" role="img" aria-label="Living room with hardwood floor" style="background:linear-gradient(180deg,#e8e6e2,#b9ada0 55%,#6b4328)"></div><div class="label">Hardwood</div></div>
<div class="abs cat" style="left:300px"><div class="photo" role="img" aria-label="Hallway with polished marble floor" style="background:linear-gradient(180deg,#d6d3cc,#bcb4a6 55%,#e3dccd)"></div><div class="label">Marble</div></div>
<div class="abs cat" style="left:600px"><div class="photo" role="img" aria-label="Lobby with grey carpet" style="background:linear-gradient(180deg,#6a6058,#8e8a86 50%,#a8a6a3)"></div><div class="label">Carpet</div></div>
<div class="abs cat" style="left:900px"><div class="photo" role="img" aria-label="Bathroom with porcelain tile" style="background:linear-gradient(180deg,#caa27a,#b58a62 55%,#d9c3a6)"></div><div class="label">Porcelain tile</div></div>

<h2 class="abs heading section-title" style="top:2005px">Featured <span>Products</span></h2>
<div class="rule" style="left:564px;top:2068px"></div>

<div class="abs product" style="left:110px;top:2111px"><div class="pic" role="img" aria-label="Light oak laminate sample" style="background:linear-gradient(135deg,#c98c3f,#e0b06b 50%,#a8692b)"><div class="tag">SALE</div></div><div class="name">PRODUCT NAME</div><div class="price">$25.00</div></div>
<div class="abs product" style="left:359px;top:2111px"><div class="pic" role="img" aria-label="Dark walnut plank sample" style="background:linear-gradient(135deg,#7a3f22,#a35a34 50%,#5c2c17)"><div class="tag">SOLD</div></div><div class="name">PRODUCT NAME</div><div class="price">$25.00</div></div>
<div class="abs product" style="left:606px;top:2111px"><div class="pic" role="img" aria-label="Waterproof wood sample with droplets" style="background:linear-gradient(135deg,#3b2a22,#5e4536 50%,#2e211b)"><div class="tag">50%</div></div><div class="name">PRODUCT NAME</div><div class="price">$25.00</div></div>
<div class="abs product" style="left:853px;top:2111px"><div class="pic" role="img" aria-label="Slate grey tile sample" style="background:linear-gradient(135deg,#4b5058,#656a72 50%,#3e4249)"><div class="tag">SALE</div></div><div class="name">PRODUCT NAME</div><div class="price">$25.00</div></div>

<div class="abs product" style="left:110px;top:2440px"><div class="pic" role="img" aria-label="White onyx marble sample" style="background:linear-gradient(135deg,#efe8df,#d8cfc3 50%,#f3eee8)"><div class="tag">SALE</div></div><div class="name">PRODUCT NAME</div><div class="price">$25.00</div></div>
<div class="abs product" style="left:359px;top:2440px"><div class="pic" role="img" aria-label="Grey striped carpet tile sample" style="background:linear-gradient(135deg,#5a5d63,#777a80 50%,#4d5055)"><div class="tag">SOLD</div></div><div class="name">PRODUCT NAME</div><div class="price">$25.00</div></div>
<div class="abs product" style="left:606px;top:2440px"><div class="pic" role="img" aria-label="Brown veined marble sample" style="background:linear-gradient(135deg,#8f7762,#c1ae98 50%,#7a6654)"><div class="tag">50%</div></div><div class="name">PRODUCT NAME</div><div class="price">$25.00</div></div>
<div class="abs product" style="left:853px;top:2440px"><div class="pic" role="img" aria-label="Beige carpet sample" style="background:linear-gradient(135deg,#b5aca1,#cfc7bc 50%,#a39a8f)"><div class="tag">SALE</div></div><div class="name">PRODUCT NAME</div><div class="price">$25.00</div></div>

<div class="abs promo" role="img" aria-label="Fan of wood flooring samples"></div>
<div class="abs promo-text" style="right:170px;top:2852px"><div class="line">Sed ut perspiciatis unde</div><div class="off">50%OFF</div></div>

<h2 class="abs heading section-title" style="top:3038px">Latest <span>Blog</span></h2>
<div class="rule" style="left:564px;top:3100px"></div>

<div class="abs post" style="left:110px"><div class="pic" role="img" aria-label="Bright living room with glossy tile floor" style="background:linear-gradient(180deg,#d9d4cc,#b2a799 55%,#8a7d6e)"><div class="date">07 May 2020</div></div><div class="title">Sed ut perspiciatis unde omnis</div><div class="body">Nemo enim ipsam voluptatem quia voluptas sit aspe matur aut odit aut fugit, sed quia consequ untur magni dolores eos qui.</div><div class="more">READ MORE</div></div>
<div class="abs post" style="left:443px"><div class="pic" role="img" aria-label="Living room with warm wood floor and fireplace" style="background:linear-gradient(180deg,#cfc5b6,#9c7f5f 55%,#6b4427)"><div class="date">07 May 2020</div></div><div class="title">Sed ut perspiciatis unde omnis</div><div class="body">Nemo enim ipsam voluptatem quia voluptas sit aspe matur aut odit aut fugit, sed quia consequ untur magni dolores eos qui.</div><div class="more">READ MORE</div></div>
<div class="abs post" style="left:778px"><div class="pic" role="img" aria-label="White family room with dark wood floor" style="background:linear-gradient(180deg,#ece9e4,#c8bfb4 55%,#6c4a32)"><div class="date">07 May 2020</div></div><div class="title">Sed ut perspiciatis unde omnis</div><div class="body">Nemo enim ipsam voluptatem quia voluptas sit aspe matur aut odit aut fugit, sed quia consequ untur magni dolores eos qui.</div><div class="more">READ MORE</div></div>

<footer class="abs footer">
  <div class="abs fcol" style="left:110px;width:200px;height:200px">
    <div class="fhead">PAYMENTS ACCEPTED</div>
    <div class="cards"><span class="card">Payway</span><span class="card">Cirqa</span><span class="card">Amplo</span><span class="card">Novapay</span></div>
    <div class="socials"><span></span><span></span><span></span><span></span><span></span></div>
  </div>
  <div class="abs fcol" style="left:377px">
    <div class="fhead">INFORMATION</div>
    <ul class="flist"><li>Sed ut perspiciatis</li><li>unde omnis iste</li><li>natus error sit</li><li>voluptatem</li><li>accusantium</li><li>doloremque</li></ul>
  </div>
  <div class="abs fcol" style="left:558px">
    <div class="fhead">CUSTOMER SERVICE</div>
    <ul class="flist"><li>Sed ut perspiciatis</li><li>unde omnis iste</li><li>natus error sit</li><li>voluptatem</li><li>accusantium</li></ul>
  </div>
  <div class="abs fcol" style="left:766px">
    <div class="fhead">MY ACCOUNT</div>
    <ul class="flist"><li>My account</li><li>Orders</li><li>Addresses</li><li>Shopping cart</li><li>Wishlist</li></ul>
  </div>
  <div class="abs fcol" style="left:922px;top:65px;width:200px">
    <div class="fhead">CONTACT US</div>
    <ul class="contact" style="margin-top:22px">
      <li><svg width="14" height="12" viewBox="0 0 14 12"><rect x="1" y="3" width="12" height="8" rx="1" fill="#fff"/><rect x="3" y="0" width="8" height="3" fill="#fff"/></svg>(000)-555-0190 (Phone)</li>
      <li><svg width="14" height="12" viewBox="0 0 14 12"><rect x="1" y="4" width="12" height="6" fill="#fff"/><rect x="3" y="0" width="8" height="4" fill="#fff"/><rect x="3" y="8" width="8" height="4" fill="#fff"/></svg>(000)-555-0190 &nbsp;(Fax)</li>
      <li><svg width="14" height="12" viewBox="0 0 14 12"><rect x="0" y="1" width="14" height="10" fill="#fff"/><path d="M0 1 L7 7 L14 1" stroke="#1f1b19" fill="none"/></svg><u>hello@floorvale.com</u></li>
      <li><svg width="14" height="14" viewBox="0 0 14 14"><path d="M7 0a5 5 0 0 1 5 5c0 4-5 9-5 9S2 9 2 5a5 5 0 0 1 5-5z" fill="#fff"/><circle cx="7" cy="5" r="2" fill="#1f1b19"/></svg>#1452 Lorem Ipsum Dummy<br>Text Lorem Ipsum</li>
    </ul>
  </div>
  <div class="abs copyright">&copy; Copyright 2020 Floorvale.All Rights Reserved</div>
</footer>

</body>
</html>
```